Custom Framing Shop Tallpine Framing Studio

I want an eye catching graphic that will be used a s business sign on a busy road. The sign MUST communicate the type of business it is clearly to vehicles traveling at 40 mph. This is a custom picture framing business and the sign will be hanging and be approximately 32" X 48". The business name is Tallpine Framing Studio; Custom framing: by appointment and should include a whole or partial image of a picture frame as a visual que. I've included inspiration idea's, color pallets and styles that I like and a current business card for inspiration. I like the crimson font style shadowing and background colors of the attached Olans pizzeria sign. I'd prefer crimson letters. Custom Framing is the message to communicate, followed by phone number and business name. I like the idea of a shield shape with a banner since it would more eye catching, Once again the Tallpine image and name is less important than communicating what the business does. I like Crimson, grey, gold, black but am open to new ideas . I like the idea of a shield with a banner more than a rectangle, but am open to idea's

Target Market(s)

My target market is local homeowners ($700k+) who want a relationship with their framer and are willing to pay for a customized experience compared to a craft store experience. I have more female clients then men.

Industry/Entity Type

Picture Framing Art

Other font styles liked:
• Look at the attached image of a custom pizzeria sign, its kid of a custom car pinstripe font style. Script and decorative may be difficult to read while driving by but add to the elegance.

Colors

Designer to choose colors to be used in the design.

Requirements
Must have
• Clearly communicate what the business does "Custom framing" preferably with a picture frame and words
Nice to have
• incorporate a Tallpine into the graphic
Should not have
• A Tallpine image doesn't communicate what the business does to a vehicle traveling at 40 mph by the sign

```html
<!DOCTYPE html>
<html lang="en">
<head>
<meta charset="utf-8">
<title>Tallpine Framing Studio – Custom Framing Sign</title>
<link rel="stylesheet" href="https://fonts.googleapis.com/css2?family=Alfa+Slab+One&family=Ultra&display=swap">
<style>
  :root {
    --crimson: #841b18;
    --gold: #c8923a;
    --charcoal: #2e2d2b;
    --cream: #f0d6ae;
    --paper: #ffffff;
  }
  html, body {
    margin: 0;
    padding: 0;
    width: 800px;
    height: 1200px;
    overflow: hidden;
    background: var(--paper);
  }
  .sign {
    display: block;
    width: 800px;
    height: 1200px;
  }
  .display-type {
    font-family: "Ultra", "Alfa Slab One", "Rockwell Extra Bold", "Arial Black", serif;
    font-weight: 900;
  }
  .brand-name { fill: var(--charcoal); font-size: 36px; letter-spacing: 2px; }
  .headline { fill: var(--charcoal); stroke: var(--charcoal); stroke-width: 5px; stroke-linejoin: round; }
  .headline-shadow { fill: var(--gold); stroke: var(--gold); stroke-width: 5px; stroke-linejoin: round; }
  .headline-gap { fill: none; stroke: var(--cream); stroke-width: 12px; stroke-linejoin: round; }
  .phone { fill: var(--cream); stroke: var(--cream); stroke-width: 4px; stroke-linejoin: round; }
  .phone-shadow { fill: var(--gold); stroke: var(--gold); stroke-width: 4px; stroke-linejoin: round; }
  .phone-gap { fill: none; stroke: var(--charcoal); stroke-width: 10px; stroke-linejoin: round; }
</style>
</head>
<body>
<svg class="sign" viewBox="0 0 800 1200" xmlns="http://www.w3.org/2000/svg">
  <defs>
    <path id="shield-outline"
      d="M3,185 L31,183 L34,172 L65,162 L65,110 L133,94 Q400,-90 666,94 L737,110 L737,162 L768,172 L771,183 L799,185 L799,857 L752,860 L752,998 Q400,1380 48,998 L48,860 L3,857 Z"/>
  </defs>

  <!-- Shield body with layered borders -->
  <g class="shield">
    <use href="#shield-outline" fill="var(--crimson)"/>
    <use href="#shield-outline" fill="var(--gold)" transform="translate(400,600) scale(.97,.98) translate(-400,-600)"/>
    <use href="#shield-outline" fill="var(--charcoal)" transform="translate(400,600) scale(.945,.962) translate(-400,-600)"/>
    <use href="#shield-outline" fill="var(--cream)" transform="translate(400,600) scale(.885,.925) translate(-400,-600)"/>
    <use href="#shield-outline" fill="none" stroke="var(--gold)" stroke-width="5" vector-effect="non-scaling-stroke"
         transform="translate(400,600) scale(.855,.9) translate(-400,-600)"/>
  </g>

  <!-- Brand line -->
  <g class="brand">
    <rect x="272" y="132" width="28" height="28" fill="none" stroke="var(--crimson)" stroke-width="4"/>
    <text class="display-type brand-name" x="312" y="163" textLength="215" lengthAdjust="spacingAndGlyphs">TALLPINE</text>
  </g>

  <!-- Headline -->
  <g class="headline-block display-type" font-size="130">
    <g aria-hidden="true">
      <text class="headline-shadow" x="142" y="352" textLength="525" lengthAdjust="spacingAndGlyphs">CUSTOM</text>
      <text class="headline-shadow" x="118" y="490" textLength="575" lengthAdjust="spacingAndGlyphs">FRAMING</text>
      <text class="headline-gap" x="136" y="337" textLength="525" lengthAdjust="spacingAndGlyphs">CUSTOM</text>
      <text class="headline-gap" x="112" y="475" textLength="575" lengthAdjust="spacingAndGlyphs">FRAMING</text>
    </g>
    <text class="headline" x="136" y="337" textLength="525" lengthAdjust="spacingAndGlyphs">CUSTOM</text>
    <text class="headline" x="112" y="475" textLength="575" lengthAdjust="spacingAndGlyphs">FRAMING</text>
  </g>

  <!-- Divider -->
  <g class="divider" fill="var(--charcoal)">
    <path d="M121,532 L390,524 L394,532 L390,534 Z"/>
    <path d="M679,532 L410,524 L406,532 L410,534 Z"/>
    <path d="M400,507 L410,523 L400,539 L390,523 Z"/>
  </g>

  <!-- Phone banner -->
  <g class="phone-banner display-type" font-size="100">
    <rect x="48" y="553" width="703" height="129" fill="var(--charcoal)"/>
    <g aria-hidden="true">
      <text class="phone-shadow" x="110" y="662" textLength="590" lengthAdjust="spacingAndGlyphs">+555019876</text>
      <text class="phone-gap" x="104" y="650" textLength="590" lengthAdjust="spacingAndGlyphs">+555019876</text>
    </g>
    <text class="phone" x="104" y="650" textLength="590" lengthAdjust="spacingAndGlyphs">+555019876</text>
  </g>

  <!-- Picture frames -->
  <g class="frames">
    <!-- back frame -->
    <g class="frame">
      <rect x="260" y="711" width="316" height="150" fill="var(--gold)"/>
      <rect x="254" y="705" width="316" height="150" fill="var(--charcoal)"/>
      <rect x="270" y="721" width="284" height="134" fill="var(--cream)"/>
      <rect x="274" y="725" width="276" height="130" fill="var(--charcoal)"/>
      <rect x="292" y="743" width="240" height="112" fill="var(--cream)"/>
      <rect x="306" y="757" width="212" height="98" fill="none" stroke="var(--gold)" stroke-width="6"/>
    </g>
    <!-- left frame -->
    <g class="frame">
      <rect x="189" y="811" width="198" height="219" rx="16" fill="var(--gold)"/>
      <rect x="183" y="805" width="198" height="219" rx="16" fill="var(--charcoal)"/>
      <rect x="199" y="821" width="166" height="187" rx="12" fill="var(--cream)"/>
      <rect x="202" y="824" width="160" height="181" rx="10" fill="var(--charcoal)"/>
      <rect x="213" y="835" width="138" height="159" rx="8" fill="var(--cream)"/>
      <rect x="222" y="844" width="120" height="141" fill="none" stroke="var(--gold)" stroke-width="6"/>
    </g>
    <!-- right frame -->
    <g class="frame">
      <rect x="447" y="855" width="176" height="175" fill="var(--gold)"/>
      <rect x="441" y="849" width="176" height="175" fill="var(--charcoal)"/>
      <rect x="458" y="866" width="142" height="141" fill="var(--cream)"/>
      <rect x="461" y="869" width="136" height="135" fill="var(--charcoal)"/>
      <rect x="470" y="878" width="118" height="117" fill="var(--cream)"/>
      <rect x="478" y="886" width="102" height="101" fill="none" stroke="var(--gold)" stroke-width="6"/>
    </g>
    <!-- front frame -->
    <g class="frame">
      <rect x="304" y="910" width="181" height="181" rx="14" fill="var(--cream)"/>
      <rect x="312" y="918" width="169" height="169" rx="12" fill="var(--gold)"/>
      <rect x="306" y="912" width="169" height="167" rx="12" fill="var(--charcoal)"/>
      <rect x="326" y="932" width="129" height="127" fill="var(--cream)"/>
      <rect x="330" y="936" width="121" height="119" fill="var(--charcoal)"/>
      <rect x="337" y="943" width="107" height="105" fill="var(--cream)"/>
      <rect x="345" y="951" width="91" height="89" fill="none" stroke="var(--gold)" stroke-width="6"/>
    </g>
  </g>
</svg>
</body>
</html>
```